Business Card Design

Personal training company in the fitness industry

Industry/Entity Type

Training

Contact Information for Business Card

(Front of card)
Peak Hour Fitness
417 Wexley Road Brookmere 6190 (Inside IronHaus365 complex)
Dario Halvorsen
Personal Trainer
halvdario@mailora.net
0412 903 548
Back of card
One on One Training
Group Training (min 3)
Outdoor bootcamps
Workout programs
Meal guides
Competition preparation
(bottom middle of card)
GET THAT HUSTLE ON!

```html
<!DOCTYPE html>
<html lang="en">
<head>
<meta charset="utf-8">
<title>Peak Hour Fitness – Business Card</title>
<link href="https://fonts.googleapis.com/css2?family=Quicksand:wght@500;600;700&display=swap" rel="stylesheet">
<style>
  :root {
    --backdrop: #d9d6d2;
    --card-dark: #1f1f1f;
    --brand-red: #ec1f24;
    --ink-white: #ffffff;
    --ink-black: #141414;
  }
  * { margin: 0; padding: 0; box-sizing: border-box; }
  html, body { width: 1200px; height: 800px; overflow: hidden; }
  body {
    background: var(--backdrop);
    font-family: "Quicksand", sans-serif;
    position: relative;
  }
  .card {
    position: absolute;
    width: 580px;
    height: 330px;
    border-radius: 24px;
    background: var(--card-dark);
    overflow: hidden;
    box-shadow: 0 14px 30px rgba(0,0,0,0.25);
  }

  /* Front */
  .card--front { left: 560px; top: 50px; }
  .brand {
    position: absolute;
    left: 40px; top: 38px;
    display: flex; align-items: center; gap: 16px;
  }
  .brand__dot {
    width: 46px; height: 46px; border-radius: 50%;
    background: var(--brand-red);
  }
  .brand__name {
    color: var(--brand-red);
    font-weight: 700;
    font-size: 30px;
    letter-spacing: 2px;
    text-transform: uppercase;
  }
  .contact {
    position: absolute;
    right: 44px; top: 130px;
    text-align: right;
    color: var(--ink-white);
    font-weight: 500;
    line-height: 1.35;
  }
  .contact__name {
    color: var(--brand-red);
    font-size: 23px;
    letter-spacing: 1.5px;
    text-transform: uppercase;
  }
  .contact__role { font-size: 18px; margin-bottom: 12px; letter-spacing: 0.5px; }
  .contact__line { font-size: 19px; letter-spacing: 1px; }
  .contact__address {
    position: absolute;
    left: 0; right: 0; bottom: 26px;
    text-align: center;
    color: var(--ink-white);
    font-size: 15px;
    font-weight: 500;
    letter-spacing: 0.3px;
  }

  /* Back */
  .card--back { left: 70px; top: 420px; }
  .services {
    position: absolute;
    left: 0; right: 0; top: 24px;
    text-align: center;
    list-style: none;
    font-weight: 600;
    font-size: 23px;
    letter-spacing: 6px;
    line-height: 1.25;
    text-transform: uppercase;
    color: var(--ink-white);
  }
  .accent { color: var(--brand-red); }
  .slogan-band {
    position: absolute;
    left: 0; right: 0; bottom: 0;
    height: 105px;
    background: var(--brand-red);
    display: flex; align-items: center; justify-content: center;
  }
  .slogan {
    color: var(--ink-black);
    font-weight: 700;
    font-size: 32px;
    letter-spacing: 3px;
    text-transform: uppercase;
  }
  .slogan__highlight { color: var(--ink-white); }
</style>
</head>
<body>

  <section class="card card--front" aria-label="Business card front">
    <div class="brand">
      <span class="brand__dot"></span>
      <span class="brand__name">Peak Hour Fitness</span>
    </div>
    <div class="contact">
      <p class="contact__name">Dario Halvorsen</p>
      <p class="contact__role">Personal Trainer</p>
      <p class="contact__line">0412 903 548</p>
      <p class="contact__line">halvdario@mailora.net</p>
    </div>
    <p class="contact__address">417 Wexley Road Brookmere 6190 (Inside IronHaus365 complex)</p>
  </section>

  <section class="card card--back" aria-label="Business card back">
    <ul class="services">
      <li><span class="accent">One on One</span> Training</li>
      <li><span class="accent">Group</span> Training <span class="accent">(min 3)</span></li>
      <li class="accent">Outdoor Bootcamps</li>
      <li>Workout Programs</li>
      <li>Meal <span class="accent">Guides</span></li>
      <li>Competition Preparation</li>
    </ul>
    <div class="slogan-band">
      <p class="slogan">Get that <span class="slogan__highlight">Hustle</span> on!</p>
    </div>
  </section>

</body>
</html>
```